Venmar Tolu Holdings Limited is a asset management company and project funding company, we specialise in high end finance for high net worth individuals, we are looking for a new logo letterhead template, email footer template and business card design. The letterhead template should be designed in word format so that the letterheading can be used electronically.

Below is the current logo that is a but plain and a little cheaper looking, colour schemes are not important just that it looks professional.

I am looking for a sharp impact that stands out,

Target Market(s)

High net worth individuals and institutions

Industry/Entity Type

Finance

Contact Information for Business Card

Venmar Tolu Holdings Limited
T: 0333 418 2960

M: 07631 942017
E:derek.hollin@venmar-toluholdings.example

CORAL MEADE, EAST HARBOUR ROAD
SECOND FLOOR, SUITE 410
P.O. BOX DK-48731
NASSAU BAHAMAS

Logo Text

Font styles to use
Serif
Sans Serif
Script
Other font styles liked:
• Tahoma

Colors
fbed22
6b449b
ec1f27
f78f20
33b8a4
0592cd

Requirements
Must have
• Colours schemes would look good in blue’s green’s purples.

Yellow and Purple together maybe a nice combination.
Nice to have
• I want the log to look sharpe, relate to a global presence, but I also want to it to look established.
Should not have
• N/a

```html
<!DOCTYPE html>
<html lang="en">
<head>
<meta charset="utf-8">
<title>Venmar Tolu Holdings Limited — Stationery</title>
<link rel="stylesheet" href="https://fonts.googleapis.com/css2?family=Jost:ital,wght@0,400;0,500;0,600;1,400;1,500&family=Yellowtail&display=swap">
<style>
  :root {
    --violet: #4a0aa6;
    --violet-deep: #33008f;
    --violet-stage: #5a25bb;
    --violet-card: #2e0a8a;
    --gold: #f5c400;
    --gold-soft: #e8c547;
    --orange: #e8662a;
    --paper: #ffffff;
    --paper-grey: #f4f4f6;
    --band: #f9f9f9;
  }
  * { margin: 0; padding: 0; box-sizing: border-box; }
  html, body { width: 1200px; height: 1200px; overflow: hidden; }
  body { font-family: "Jost", sans-serif; background: var(--violet-deep); position: relative; }

  .brand-band { position: absolute; left: 0; top: 0; width: 1200px; height: 361px; background: var(--band); }
  .brand-lockup { position: absolute; left: 312px; top: 56px; display: flex; align-items: center; gap: 34px; }
  .brand-mark { width: 260px; height: 260px; border-radius: 50%;
    background: radial-gradient(circle at 70% 45%, #fff200 0%, var(--gold) 35%, var(--orange) 85%); }
  .brand-name { font-weight: 500; font-size: 60px; line-height: 1.05; color: var(--violet); }

  .stage { position: absolute; left: 55px; top: 361px; width: 1093px; height: 839px; background: var(--violet-stage); }

  .letterhead { position: absolute; left: 267px; top: 490px; width: 447px; height: 620px;
    background: linear-gradient(180deg, var(--paper) 0%, var(--paper) 30%, var(--paper-grey) 100%);
    box-shadow: 0 6px 18px rgba(20,0,60,.35); }
  .letterhead-logo { position: absolute; right: 28px; top: 20px; display: flex; align-items: center; gap: 6px; }
  .letterhead-logo .dot { width: 28px; height: 28px; border-radius: 50%;
    background: radial-gradient(circle at 65% 45%, #fff200, var(--gold) 40%, var(--orange)); }
  .letterhead-logo .name { font-size: 9.5px; font-weight: 500; line-height: 1.1; color: var(--violet); }
  .letterhead-contact { position: absolute; left: 30px; right: 26px; bottom: 30px; display: flex; align-items: flex-end;
    gap: 12px; font-size: 6.6px; font-style: italic; font-weight: 500; color: var(--violet); }
  .contact-item { display: flex; align-items: center; gap: 3px; white-space: nowrap; }
  .contact-item svg { flex: none; fill: var(--violet); }
  .letterhead-wave { position: absolute; left: 0; bottom: 0; width: 447px; height: 24px; }

  .card { position: absolute; left: 775px; width: 265px; height: 140px; box-shadow: 0 5px 14px rgba(20,0,60,.4); overflow: hidden; }
  .card-front { top: 499px; background: linear-gradient(120deg, #22067a 0%, var(--violet-card) 45%, #3a0099 100%); color: #fff; }
  .card-front .dot { position: absolute; left: 110px; top: 42px; width: 46px; height: 46px; border-radius: 50%;
    background: radial-gradient(circle at 65% 45%, #fff200, var(--gold) 40%, var(--orange)); }
  .card-front .name { position: absolute; left: 0; right: 0; top: 94px; text-align: center; font-size: 9.5px; font-weight: 500; letter-spacing: .3px; }
  .card-front .phone { position: absolute; left: 0; right: 0; top: 109px; display: flex; justify-content: center; align-items: center; gap: 5px;
    font-size: 7px; letter-spacing: 1px; font-style: italic; }
  .card-front .rule { width: 22px; height: 3px; border-top: 1px solid var(--gold-soft); border-bottom: 1px solid var(--gold-soft); }

  .card-back { top: 669px; background: var(--paper); }
  .card-back .wash { position: absolute; left: 0; top: 0; width: 180px; height: 140px;
    background: linear-gradient(135deg, #e6dcf6 0%, #f3eefb 45%, #fbf4e2 75%, rgba(255,255,255,0) 100%); }
  .card-back .person { position: absolute; right: 52px; top: 22px; text-align: right; color: var(--violet); }
  .card-back .first { font-family: "Yellowtail", cursive; font-size: 38px; line-height: .9; }
  .card-back .last { font-size: 9px; font-weight: 600; letter-spacing: .5px; margin-top: -2px; }
  .card-back .details { position: absolute; right: 42px; top: 82px; text-align: right; font-size: 5.4px; font-style: italic; font-weight: 500;
    line-height: 1.55; color: var(--violet); }
  .card-back .icon-strip { position: absolute; right: 34px; top: 82px; width: 7px; height: 38px; background: var(--violet); }
</style>
</head>
<body>
  <header class="brand-band">
    <div class="brand-lockup">
      <div class="brand-mark"></div>
      <div class="brand-name">Venmar Tolu<br>Holdings Limited</div>
    </div>
  </header>

  <main class="stage"></main>

  <section class="letterhead" aria-label="Letterhead">
    <div class="letterhead-logo">
      <div class="dot"></div>
      <div class="name">Venmar Tolu<br>Holdings Limited</div>
    </div>
    <div class="letterhead-contact">
      <div class="contact-item">
        <svg width="6" height="9" viewBox="0 0 6 9"><rect x="0" y="0" width="6" height="9" rx="1"/></svg>
        0333 418 2960
      </div>
      <div class="contact-item">
        <svg width="10" height="7" viewBox="0 0 10 7"><rect width="10" height="7" rx="1"/><path d="M0.5 0.8 5 4 9.5 0.8" stroke="#fff" stroke-width="0.9" fill="none"/></svg>
        derek.hollin@venmar-toluholdings.example
      </div>
      <div class="contact-item">
        <svg width="7" height="10" viewBox="0 0 7 10"><path d="M3.5 0a3.5 3.5 0 0 1 3.5 3.5C7 6 3.5 10 3.5 10S0 6 0 3.5A3.5 3.5 0 0 1 3.5 0z"/><circle cx="3.5" cy="3.5" r="1.3" fill="#fff"/></svg>
        <span>Coral Meade, East Harbour Road, Second Floor,<br>Suite 410 P.O. Box DK-48731 Nassau Bahamas</span>
      </div>
    </div>
    <svg class="letterhead-wave" viewBox="0 0 447 24" preserveAspectRatio="none">
      <path d="M0 24 L0 15 Q220 14 447 4 L447 24 Z" fill="#e8c547"/>
      <path d="M0 15 Q220 14 447 4 L447 7 Q220 17 0 18 Z" fill="#4a0aa6"/>
    </svg>
  </section>

  <section class="card card-front" aria-label="Business card front">
    <div class="dot"></div>
    <div class="name">Venmar Tolu Holdings Limited</div>
    <div class="phone"><span class="rule"></span>0333 418 2960<span class="rule"></span></div>
  </section>

  <section class="card card-back" aria-label="Business card back">
    <div class="wash"></div>
    <div class="person">
      <div class="first">Derek</div>
      <div class="last">HOLLIN</div>
    </div>
    <div class="details">
      07631 942017<br>
      derek.hollin@venmar-toluholdings.example<br>
      Coral Meade, East Harbour Road, Second Floor,<br>
      Suite 410 P.O. Box DK-48731<br>
      Nassau Bahamas
    </div>
    <div class="icon-strip"></div>
  </section>
</body>
</html>
```